Aviation security consulting company needs a website

We need a website design for Brell Ostavik, and aviation security consulting company. Brell Ostavik (www.brellostavik.example) is an aviation security consulting company that works with government and industry stakeholders in over 60 countries on aviation security strategy, governance, and oversight at the regulatory and operational level.
Brell Ostavik is strongly internationally focused.
The website required should be simple, corporate, serious, and communicate professionalism, reliability and honesty. We are trying to give the company a feeling of being well established.
The attached files include the company logo, along with examples of company web page styles that we like.
The Brell Ostavik website need only be around five pages long (landing page, who we are, our services, our clients, contact), though don't feel limited to only five pages.
The existing website (www.brellostavik.example) was rushed and put together using Wix. We don't love the existing website as it looks too amateur, so don't use it as a template.
There is no requirement for any online sales tools to be included in the site. The site is purely informational, with the option of people making contact via email.

```html
<!DOCTYPE html>
<html lang="en">
<head>
<meta charset="utf-8">
<title>Brell Ostavik — Practice Areas</title>
<link rel="stylesheet" href="https://fonts.googleapis.com/css2?family=Montserrat:wght@400;500;600&family=Raleway:wght@400;500&display=swap">
<style>
  :root {
    --navy-deep: #0a1530;
    --navy-hero-top: #3c4f78;
    --navy-hero-bottom: #1b2849;
    --tile-light: rgba(238, 239, 243, 0.95);
    --ink-dark: #101a33;
    --ink-body: #1d2743;
    --white: #ffffff;
    --muted-blue: #6e81a8;
    --muted-blue-strong: #7f92b8;
  }
  * { box-sizing: border-box; margin: 0; padding: 0; }
  html, body { width: 1200px; height: 821px; overflow: hidden; }
  body {
    position: relative;
    font-family: "Montserrat", sans-serif;
    background: var(--navy-deep);
    color: var(--white);
  }

  .site-header {
    position: absolute; left: 0; top: 0; width: 1200px; height: 96px;
    background: var(--navy-deep);
  }
  .brand {
    position: absolute; left: 96px; top: 22px; height: 53px;
    display: flex; align-items: center; gap: 12px;
  }
  .brand-mark { width: 53px; height: 53px; background: var(--white); }
  .brand-name {
    font-family: "Montserrat", sans-serif; font-weight: 500;
    font-size: 29px; letter-spacing: -0.5px; color: var(--white);
  }
  .main-nav {
    position: absolute; right: 93px; top: 34px;
    display: flex; gap: 35px;
  }
  .main-nav a {
    color: var(--white); text-decoration: none;
    font-size: 16px; font-weight: 400;
  }

  .hero {
    position: absolute; left: 0; top: 96px; width: 1200px; height: 682px;
    background: linear-gradient(180deg, var(--navy-hero-top) 0%, #2e4068 45%, var(--navy-hero-bottom) 100%);
  }

  .practice-grid {
    position: absolute; left: 186px; top: 236px;
    width: 829px; height: 370px;
    display: grid; grid-template-columns: 277px 277px 275px; grid-template-rows: 185px 185px;
  }
  .tile { position: relative; overflow: hidden; }
  .tile--light { background: var(--tile-light); color: var(--ink-body); }
  .tile-photo { position: absolute; inset: 0; }
  .tile-photo--terminal { background: linear-gradient(180deg, #3b4866 0%, #2a3550 60%, #1c2438 100%); }
  .tile-photo--cargo { background: linear-gradient(180deg, #3c4a70 0%, #2b375a 55%, #1b2440 100%); }
  .tile-photo--cabin { background: linear-gradient(180deg, #4a5a82 0%, #2f3c5e 55%, #161d30 100%); }
  .tile-body { position: absolute; left: 0; top: 0; width: 100%; padding: 24px 24px 0 24px; }
  .tile-title { font-size: 17.5px; font-weight: 500; line-height: 1.2; }
  .tile--light .tile-title { color: var(--ink-dark); }
  .tile-text { margin-top: 8px; font-size: 12.5px; line-height: 15.5px; font-weight: 400; }
  .tile--dark .tile-text { color: #e6e9f2; }
  .tile--intro .tile-title { font-size: 23px; font-weight: 600; padding-top: 2px; }

  .hero-tagline {
    position: absolute; left: 0; top: 655px; width: 1210px;
    text-align: center; font-size: 15px; line-height: 19px;
    color: var(--muted-blue);
  }
  .hero-tagline strong { font-weight: 600; color: var(--muted-blue-strong); }

  .site-footer {
    position: absolute; left: 0; top: 778px; width: 1200px; height: 43px;
    background: var(--navy-deep);
    font-family: "Raleway", sans-serif; font-size: 10.5px; color: var(--white);
  }
  .copyright { position: absolute; left: 96px; top: 19px; }
  .legal-links { position: absolute; right: 94px; top: 18px; display: flex; gap: 6px; }
  .legal-links a { color: var(--white); text-decoration: none; }
</style>
</head>
<body>
  <header class="site-header">
    <div class="brand">
      <span class="brand-mark" aria-hidden="true"></span>
      <span class="brand-name">Brell Ostavik</span>
    </div>
    <nav class="main-nav">
      <a href="#">Home</a>
      <a href="#">Who We Are</a>
      <a href="#">Our Services</a>
      <a href="#">Our Clients</a>
      <a href="#">Contact</a>
    </nav>
  </header>

  <section class="hero" role="img" aria-label="Underside view of a passenger jet taking off over a runway under a cloudy sky, tinted dark blue"></section>

  <section class="practice-grid">
    <article class="tile tile--light tile--intro">
      <div class="tile-body"><h1 class="tile-title">Practice Areas</h1></div>
    </article>
    <article class="tile tile--dark">
      <div class="tile-photo tile-photo--terminal" role="img" aria-label="Travellers silhouetted against a terminal window overlooking aircraft"></div>
      <div class="tile-body" style="padding:26px 24px 0 16px">
        <h2 class="tile-title">Regulators</h2>
        <p class="tile-text" style="padding-left:2px">Strategic guidance, development of regulation, training, mentoring, and developing aviation security compliance tools.</p>
      </div>
    </article>
    <article class="tile tile--light">
      <div class="tile-body" style="padding:28px 24px 0 22px">
        <h2 class="tile-title">Capacity Development</h2>
        <p class="tile-text">Implementing economically sustainable solutions to aviation security challenges in the local environment.</p>
      </div>
    </article>
    <article class="tile tile--dark">
      <div class="tile-photo tile-photo--cargo" role="img" aria-label="Cargo aircraft on the apron with boarding stairs and ground vehicles at dusk"></div>
      <div class="tile-body" style="padding:24px 24px 0 24px">
        <h2 class="tile-title">Air Cargo</h2>
        <p class="tile-text" style="padding-left:2px">Assisting air cargo operators meet aviation security obligations while ensuring facilitation and profitability are maintained.</p>
      </div>
    </article>
    <article class="tile tile--light">
      <div class="tile-body" style="padding:26px 24px 0 24px">
        <h2 class="tile-title">Airports</h2>
        <p class="tile-text">Ensuring security is incorporated into airport design, conducting security assessments and undertaking strategic planning.</p>
      </div>
    </article>
    <article class="tile tile--dark">
      <div class="tile-photo tile-photo--cabin" role="img" aria-label="Empty aircraft cabin aisle between rows of seats"></div>
      <div class="tile-body" style="padding:24px 24px 0 21px">
        <h2 class="tile-title">Airlines</h2>
        <p class="tile-text" style="padding-left:2px">Developing programs, conducting assessments, and provide strategic guidance, governance and change management.</p>
      </div>
    </article>
  </section>

  <p class="hero-tagline"><strong>Brell Ostavik</strong> works with government and industry on aviation<br>security regulatory and operational strategy, governance, and oversight.</p>

  <footer class="site-footer">
    <p class="copyright">© 2016. Brell Ostavik. All Rights Reserved.</p>
    <nav class="legal-links"><a href="#">Terms</a><span>|</span><a href="#">Privacy Policy</a></nav>
  </footer>
</body>
</html>
```